Customized cakes and cupcakes for all kind of occasions

hello below attached will be the logo of my bakery..

i would like the some designs for some cake boxes, starting from 8 inch square till 16 inches.

i will also need some small boxes for cookies and other desserts.

i would love to see the box with the logo and some creative ideas..

Target Market(s)

young adults

Industry/Entity Type

Bakery

Colors
85cae6
d2a4cc
eea4c8
fae0ec
ffffff
e4daeb
cfeae6
dbdbdb

Requirements
Must have
• the logo
Nice to have
• pastel colors

```html
<!DOCTYPE html>
<html lang="en">
<head>
<meta charset="utf-8">
<title>Cakes and Cupcakes Lagoon 1 — Box Set</title>
<link rel="stylesheet" href="https://fonts.googleapis.com/css2?family=Source+Sans+3:wght@300;400&family=Libre+Baskerville:wght@400;700&display=swap">
<style>
  :root {
    --paper: #ffffff;
    --ink: #111111;
    --lagoon: #7fcdc5;
    --lagoon-deep: #0a9396;
    --frosting: #ffffff;
    --chocolate: #5a2320;
    --leader: #666666;
  }
  * { margin: 0; padding: 0; box-sizing: border-box; }
  html, body {
    width: 1126px;
    height: 1200px;
    overflow: hidden;
    background: var(--paper);
  }
  .sheet {
    position: relative;
    width: 1126px;
    height: 1200px;
    font-family: "Source Sans 3", "Myriad Pro", sans-serif;
    font-weight: 300;
    color: var(--ink);
  }
  .sheet-title {
    position: absolute;
    left: 68px;
    top: 64px;
    font-size: 47px;
    font-weight: 300;
    letter-spacing: -0.3px;
  }
  .leaders {
    position: absolute;
    inset: 0;
    width: 1126px;
    height: 1200px;
    pointer-events: none;
  }
  .leaders line, .leaders polyline {
    stroke: var(--leader);
    stroke-width: 1.2;
    fill: none;
  }

  /* colour swatch */
  .swatch {
    position: absolute;
    left: 884px;
    top: 68px;
    width: 212px;
    height: 282px;
    background: var(--lagoon);
    font-family: "Libre Baskerville", serif;
    text-align: center;
  }
  .swatch-name {
    margin-top: 122px;
    font-size: 13px;
    font-weight: 700;
    font-variant: small-caps;
    letter-spacing: 1.5px;
  }
  .swatch-values {
    margin-top: 10px;
    font-size: 7.5px;
    font-weight: 700;
    letter-spacing: 0.6px;
  }

  /* box faces */
  .face {
    position: absolute;
    background: var(--lagoon);
  }
  .face-top {
    left: 367px;
    top: 198px;
    width: 391px;
    height: 392px;
  }
  .brand-mark {
    position: absolute;
    inset: 0;
    display: flex;
    align-items: center;
    justify-content: center;
    flex-direction: column;
    gap: 0;
  }
  .brand-ring {
    position: absolute;
    left: 79px;
    top: 80px;
    width: 232px;
    height: 232px;
    border: 2px solid var(--frosting);
    border-radius: 50%;
  }
  .brand-name {
    position: relative;
    color: var(--frosting);
    font-size: 30px;
    font-weight: 400;
    letter-spacing: 3px;
    text-transform: uppercase;
    text-align: center;
    line-height: 1.25;
  }

  .face-side {
    top: 686px;
    width: 392px;
    height: 391px;
    background: var(--paper);
  }
  .face-side.first { left: 138px; }
  .face-side.second { left: 595px; }
  .cake-illustration {
    position: absolute;
    left: 0;
    top: 0;
    width: 392px;
    height: 196px;
    background: linear-gradient(
      to bottom,
      var(--lagoon) 0%,
      var(--lagoon) 18%,
      var(--frosting) 30%,
      var(--frosting) 58%,
      var(--chocolate) 66%,
      var(--chocolate) 80%,
      var(--lagoon-deep) 82%,
      var(--lagoon-deep) 100%
    );
  }
  .stripe {
    position: absolute;
    left: 0;
    width: 392px;
    height: 30px;
    background: var(--lagoon-deep);
  }
  .stripe:nth-of-type(2) { top: 213px; }
  .stripe:nth-of-type(3) { top: 263px; }
  .stripe:nth-of-type(4) { top: 312px; }
  .stripe:nth-of-type(5) { top: 361px; }

  .face-label {
    position: absolute;
    font-size: 28px;
    font-weight: 300;
    text-align: center;
    width: 392px;
  }
  .face-label sup { font-size: 15px; }
  .label-top { left: 367px; top: 604px; }
  .label-first { left: 138px; top: 1106px; }
  .label-second { left: 595px; top: 1106px; }

  .note {
    position: absolute;
    left: 35px;
    top: 503px;
    font-size: 17px;
    font-weight: 300;
    letter-spacing: -0.2px;
  }
</style>
</head>
<body>
<main class="sheet">
  <h1 class="sheet-title">Cakes and Cupcakes Lagoon 1</h1>

  <section class="face face-top" aria-label="Top side of the box">
    <div class="brand-ring"></div>
    <div class="brand-mark">
      <p class="brand-name">Lumi's<br>Bakery</p>
    </div>
  </section>
  <p class="face-label label-top">Top side of the box</p>

  <aside class="swatch" aria-label="Colour reference">
    <p class="swatch-name">Lagoon Blue.</p>
    <p class="swatch-values">50.24, 0, 26.63, 0</p>
  </aside>

  <section class="face face-side first" aria-label="First side of the box">
    <div class="cake-illustration" role="img" aria-label="Illustration of a chocolate cake with white frosting, sprinkles and a red cherry on top, above a scalloped teal border"></div>
    <div class="stripe"></div>
    <div class="stripe"></div>
    <div class="stripe"></div>
    <div class="stripe"></div>
  </section>
  <p class="face-label label-first">1<sup>st</sup> side of the box</p>

  <section class="face face-side second" aria-label="Second side of the box">
    <div class="cake-illustration" role="img" aria-label="Illustration of a chocolate cake with white frosting, sprinkles and a red cherry on top, above a scalloped teal border"></div>
    <div class="stripe"></div>
    <div class="stripe"></div>
    <div class="stripe"></div>
    <div class="stripe"></div>
  </section>
  <p class="face-label label-second">2<sup>nd</sup> side of the box</p>

  <p class="note">A BIT DARKER from Lagoon</p>

  <svg class="leaders" viewBox="0 0 1126 1200" aria-hidden="true">
    <line x1="912" y1="303" x2="736" y2="417"/>
    <line x1="912" y1="303" x2="912" y2="710"/>
    <polyline points="73,525 73,913 176,913"/>
  </svg>
</main>
</body>
</html>
```